The Wardrobe Sage needs a business card

The wardrobe sage is a lead generation service serving the Custom Closet industry.

Here is the basic card information:

The Wardrobe Sage
Dorian Pettigrew
Owner/CEO
Charlotte, NC
704-318-5527 Cell
Email: dpettigrew@TheWardrobeSage.com

Additional information for the card:

"High quality, flat rate lead generation exclusively for the custom closet industry"

Bullet points for the back:

- Low fixed cost
- Easy to budget
- Guaranteed qualified Leeds
- Exclusivity per city

Logo attached, head shot attached. Photos of closet systems attached

```html
<!DOCTYPE html>
<html lang="en">
<head>
<meta charset="utf-8">
<title>The Wardrobe Sage – Business Card</title>
<link rel="stylesheet" href="https://fonts.googleapis.com/css2?family=Libre+Baskerville:wght@400;700&display=swap">
<style>
  :root {
    --bronze: #a0632f;
    --paper: #ffffff;
    --ink: #1e1e1e;
    --slate: #4a4a4a;
    --backdrop: #c4c4c4;
  }
  * { box-sizing: border-box; margin: 0; padding: 0; }
  html, body {
    width: 1200px; height: 815px; overflow: hidden;
    background: var(--backdrop);
    font-family: "Libre Baskerville", Georgia, serif;
  }
  .stage {
    position: relative; width: 1200px; height: 815px;
    display: flex; align-items: center; justify-content: center; gap: 40px;
  }
  .card {
    position: relative; width: 540px; height: 309px;
    border-radius: 26px; overflow: hidden;
  }
  .card--front {
    background: var(--paper);
    border: 2px solid var(--bronze);
  }
  .card--back {
    background: var(--bronze);
    color: var(--paper);
    display: flex; flex-direction: column; align-items: center; justify-content: center;
  }
  .brand {
    position: absolute; top: 42px; right: 50px;
    display: flex; align-items: center; gap: 10px;
    color: var(--bronze); font-size: 22px; font-weight: 400;
  }
  .brand__dot {
    width: 12px; height: 12px; border-radius: 50%; background: var(--bronze);
  }
  .person { position: absolute; left: 46px; top: 178px; }
  .person__name { color: var(--bronze); font-size: 25px; font-weight: 700; letter-spacing: .3px; }
  .person__title { color: var(--ink); font-size: 13px; margin-top: 4px; }
  .location {
    position: absolute; right: 46px; top: 210px;
    font-size: 12px; color: var(--slate);
  }
  .divider {
    position: absolute; left: 46px; right: 46px; top: 234px;
    height: 1px; background: var(--ink);
  }
  .contact {
    position: absolute; left: 46px; top: 246px;
    list-style: none; font-size: 13px; color: var(--ink);
  }
  .contact__item { display: flex; align-items: center; gap: 10px; height: 22px; }
  .contact__icon { width: 14px; height: 14px; fill: var(--bronze); }
  .back-brand {
    display: flex; align-items: center; gap: 14px;
    font-size: 38px; font-weight: 400; margin-bottom: 34px;
  }
  .back-brand__dot { width: 18px; height: 18px; border-radius: 50%; background: var(--paper); }
  .benefits { list-style: none; text-align: center; font-size: 18px; line-height: 1.5; }
  .benefits__sep { margin: 0 8px; }
</style>
</head>
<body>
<main class="stage">
  <section class="card card--front" aria-label="Card front">
    <div class="brand"><span class="brand__dot"></span>The Wardrobe Sage</div>
    <div class="person">
      <p class="person__name">Dorian Pettigrew</p>
      <p class="person__title">Owner/CEO</p>
    </div>
    <p class="location">Charlotte, NC</p>
    <div class="divider"></div>
    <ul class="contact">
      <li class="contact__item">
        <svg class="contact__icon" viewBox="0 0 24 24" aria-hidden="true"><path d="M6.6 10.8a15.1 15.1 0 0 0 6.6 6.6l2.2-2.2a1 1 0 0 1 1-.25 11.4 11.4 0 0 0 3.6.57 1 1 0 0 1 1 1V20a1 1 0 0 1-1 1A17 17 0 0 1 3 4a1 1 0 0 1 1-1h3.5a1 1 0 0 1 1 1c0 1.25.2 2.45.57 3.57a1 1 0 0 1-.25 1z"/></svg>
        704-318-5527
      </li>
      <li class="contact__item">
        <svg class="contact__icon" viewBox="0 0 24 24" aria-hidden="true"><path d="M2 5h20v14H2zm2 2v.5l8 5 8-5V7zm0 2.9V17h16V9.9l-8 5z"/></svg>
        dpettigrew@TheWardrobeSage.com
      </li>
    </ul>
  </section>

  <section class="card card--back" aria-label="Card back">
    <div class="back-brand"><span class="back-brand__dot"></span>The Wardrobe Sage</div>
    <ul class="benefits">
      <li>• Low fixed cost <span class="benefits__sep">•</span> Easy to budget</li>
      <li>• Guaranteed qualified Leeds</li>
      <li>• Exclusivity per city</li>
    </ul>
  </section>
</main>
</body>
</html>
```